Web Design Project - (DESIGN AND FOLLOW UP CODING)

Web design for new management consultancy company

**About The Halvern Group

We work with organisations find and implement creative and sensible solutions...

We explore and inform…We have in-house research capability and enrich discussion through our own research, analysis and inputs. We interview staff and stakeholders, analyse data and literature and help you develop knowledge and solutions, and the plans to implement these.

We present new ideas…We develop proposals and reports that use internally and externally derived evidence to propose effective new solutions.

Specialties
Higher Education, TAFE, Local Government, Regional Development

Industry
Education Management
Updates

Target Market(s)

Business and government managers

Industry/Entity Type

Education

Requirements
Must have
• Sections:

**About
We work with organisations find and implement solutions to opportunities and challenges.
We explore and inform…
We present new ideas…

We develop proposals and reports that link internally and externally derived evidence to develop and implement new solutions.

Our three practice pillars are-
Ideas and partnerships:
Knowledgeable leaders:
Solutions:

** People
Martin Colbey (PHOTO) Bio

** Services
Acumen - Solutions - Partnerships -Implementation
- On time and within budget.
- Project leadership.
- Researched inputs and facilitated outcomes.
- Focus on implementation.
- Develop value-adding partnerships and get them funded
- Creative responses to funding opportunities
- Organisational reviews

Sectors
-Education
-State Government
- Local Government
- Utilities
- Financial services
- Health and ageing
- Human services
- Government
-Regional

** Careers

** Key Partners
With weblinks

** Contact

Links to Twitter LinkedIn Facebook
Nice to have
• Logo available from: quillmark@zevonet.com.au

```html
<!DOCTYPE html>
<html lang="en">
<head>
<meta charset="utf-8">
<title>The Halvern Group</title>
<link href="https://fonts.googleapis.com/css2?family=Ubuntu:wght@300;400;500;700&family=Roboto:wght@400;500&display=swap" rel="stylesheet">
<style>
  :root{
    --orange:#e8562a;
    --blue:#17618a;
    --blue-dark:#125a82;
    --footer:#1b6a93;
    --text:#2b2b2b;
    --rule:#cfcfcf;
    --partners-bg:#efefef;
    --partner-mark:#c4c4c4;
  }
  *{box-sizing:border-box;margin:0;padding:0}
  html,body{width:1200px;height:1162px;overflow:hidden;background:#fff}
  body{position:relative;font-family:Roboto,Arial,sans-serif;color:var(--text);font-size:11.5px}
  ul{list-style:none}
  .abs{position:absolute}

  /* header */
  .site-header{left:0;top:0;width:1200px;height:84px;border-bottom:2px solid #e6e6e6}
  .brand{left:212px;top:28px;display:flex;align-items:center;gap:10px}
  .brand-square{width:26px;height:26px;background:var(--blue-dark)}
  .brand-name{font-family:Ubuntu,sans-serif;font-weight:400;font-size:20px;color:var(--blue-dark);line-height:26px}
  .main-nav{right:225px;top:36px;display:flex;gap:29px}
  .main-nav a{font-family:Ubuntu,sans-serif;font-size:14px;color:var(--orange);text-decoration:none}

  /* hero */
  .hero{left:0;top:86px;width:1200px;height:357px;background:linear-gradient(90deg,#dfe9ef 0%,#c8d7e0 35%,#b7c9d4 55%,#8ea6b6 70%,#c6d3db 100%)}
  .hero-photo{left:730px;top:86px;width:470px;height:306px;background:radial-gradient(ellipse at 45% 45%,#d8b6a0 0%,#b58f78 30%,#2b3a4d 75%,#33465c 100%);opacity:.85}
  .hero-copy{left:212px;top:163px;font-family:Ubuntu,sans-serif;font-weight:300;font-size:14.5px;line-height:25.7px;color:#33506a}
  .cta-band{left:0;top:392px;width:1200px;height:51px;background:rgba(18,92,134,.93)}
  .cta-text{left:212px;top:16px;font-family:Ubuntu,sans-serif;font-weight:300;font-size:13.5px;color:#fff;letter-spacing:-.2px}
  .cta-button{left:931px;top:14px;width:58px;height:23px;background:var(--orange);color:#fff;font-size:9.5px;font-weight:500;display:flex;align-items:center;justify-content:center}

  /* sections */
  .section-title{font-family:Ubuntu,sans-serif;font-size:20px;color:var(--blue-dark);font-weight:400}
  .section-title small{font-size:12px;color:var(--orange);margin-left:3px}
  .rule{height:1px;background:var(--rule)}
  .body-text{font-size:11.5px;line-height:18px;color:var(--text)}
  .bullets li{position:relative;padding-left:16px;line-height:18px}
  .bullets li::before{content:"";position:absolute;left:1px;top:7px;width:4px;height:4px;background:#333}

  .about{left:212px;top:504px;width:377px}
  .about .rule{margin-top:10px}
  .about p{margin-top:16px}
  .pillars{display:flex;margin-top:14px}
  .pillars > span{width:184px}

  .people-photo{left:611px;top:494px;width:178px;height:162px;background:radial-gradient(ellipse at 50% 40%,#9a9a9a 0%,#6d6d6d 35%,#d8d8d8 80%,#f2f2f2 100%)}
  .people{left:811px;top:504px;width:178px}
  .people .rule{margin-top:10px}
  .person-facts{margin-top:16px}
  .person-facts li{display:flex;gap:8px;line-height:18px}
  .person-facts svg{flex:none;margin-top:3px}
  .person-name{font-weight:500}
  .people-rule{left:611px;top:677px;width:378px}

  .tabs{left:212px;top:709px;width:377px}
  .tab-bar{display:flex;height:49px}
  .tab{font-family:Ubuntu,sans-serif;font-size:14px;display:flex;align-items:center;padding:0 14px;border:1px solid var(--rule);border-bottom:none}
  .tab.active{border-top:2px solid var(--orange);background:#fff;position:relative;z-index:2;height:50px}
  .tab.inactive{background:#f0f0f0;margin-left:2px}
  .tab-panel{border:1px solid var(--rule);height:175px;padding:14px 16px 0 32px;position:relative}
  .tab-panel .more{position:absolute;right:12px;top:10px;color:var(--orange);font-size:11.5px}
  .tab-panel .bullets{margin-top:6px}

  .panel-head{display:flex;justify-content:space-between;align-items:center;height:30px}
  .pager{display:flex;gap:3px}
  .pager span{width:26px;height:30px;background:#ededed;display:flex;align-items:center;justify-content:center}
  .quotes{left:611px;top:721px;width:178px}
  .quotes .rule,.careers .rule{margin-top:8px}
  .quote-text{margin-top:16px;text-indent:42px;line-height:18px;position:relative}
  .quote-mark{position:absolute;left:17px;top:4px}
  .quote-by{text-align:right;font-style:italic;margin-top:14px}
  .quote-role{text-align:right;font-size:6px;letter-spacing:.3px}

  .careers{left:811px;top:721px;width:178px}
  .job{border-bottom:1px dashed #bdbdbd;padding:6px 0 5px;line-height:18px}
  .job:first-of-type{padding-top:16px}
  .job a{color:var(--orange);text-decoration:none;display:block}
  .job em{display:block}
  .all-offers{color:var(--orange);margin-top:4px;display:block;text-decoration:none}

  .partners-title{left:212px;top:973px}
  .partners-title .section-title{font-size:17px}
  .partners{left:0;top:1003px;width:1200px;height:72px;background:var(--partners-bg)}
  .partner-row{position:absolute;left:232px;top:22px;display:flex;gap:44px;align-items:center}
  .partner-mark{background:var(--partner-mark);border-radius:3px}

  .site-footer{left:0;top:1075px;width:1200px;height:87px;background:var(--footer);color:#fff}
  .contact-line{left:212px;top:33px;font-family:Ubuntu,sans-serif;font-weight:300;font-size:14.5px}
  .legal{left:212px;top:63px;font-size:6.5px;display:flex;gap:46px}
  .connect{left:811px;top:32px;display:flex;align-items:center;gap:14px;font-family:Ubuntu,sans-serif;font-weight:300;font-size:14.5px}
  .social{display:flex;gap:9px}
  .social span{width:20px;height:20px;border-radius:50%;background:#fff}
</style>
</head>
<body>

<header class="site-header abs">
  <div class="brand abs">
    <span class="brand-square"></span>
    <span class="brand-name">The Halvern Group</span>
  </div>
  <nav class="main-nav abs">
    <a href="#">About</a><a href="#">People</a><a href="#">Services</a><a href="#">Careers</a><a href="#">Key partners</a><a href="#">Contact</a>
  </nav>
</header>

<section class="hero abs" role="img" aria-label="Bright office interior, softly blurred"></section>
<div class="hero-photo abs" role="img" aria-label="Portrait of a smiling consultant in a suit"></div>
<div class="hero-copy abs">
  We work with organisations find and implement solutions to<br>
  opportunities and challenges.<br>
  We explore and inform…<br>
  We present new ideas…
</div>
<div class="cta-band abs">
  <div class="cta-text abs">Call to action line, great visual hierarchy. We already know how to help grow your business…</div>
  <div class="cta-button abs">Hire us!</div>
</div>

<section class="about abs">
  <h2 class="section-title">About us <small>more +</small></h2>
  <div class="rule"></div>
  <p class="body-text">We develop proposals and reports that link internally and externally derived evidence to develop and implement new solutions.</p>
  <div class="pillars body-text">
    <span>Our three practice pillars are:</span>
    <ul class="bullets"><li>Ideas and partnerships</li><li>Knowledgeable leaders</li><li>Solutions</li></ul>
  </div>
</section>

<div class="people-photo abs" role="img" aria-label="Black and white portrait of Martin Colbey"></div>
<section class="people abs">
  <h2 class="section-title">People <small>all +</small></h2>
  <div class="rule"></div>
  <ul class="person-facts body-text">
    <li><svg width="11" height="11" viewBox="0 0 11 11"><circle cx="5.5" cy="3" r="2.6" fill="#333"/><path d="M0.5 11c0-3 2.2-4.6 5-4.6s5 1.6 5 4.6z" fill="#333"/></svg><span class="person-name">Martin Colbey</span></li>
    <li><svg width="11" height="11" viewBox="0 0 11 11"><rect x="0.5" y="3" width="10" height="7" fill="#333"/><rect x="3.5" y="1" width="4" height="2.5" fill="none" stroke="#333"/></svg><span>CEO</span></li>
    <li><svg width="11" height="11" viewBox="0 0 11 11"><path d="M1 10L10 1" stroke="#333" stroke-width="2"/></svg><span>Leading expert on strategy development, policy reform and operating model design initiatives for public sector.</span></li>
  </ul>
</section>
<div class="people-rule rule abs"></div>

<section class="tabs abs">
  <div class="tab-bar">
    <div class="tab active">Services</div>
    <div class="tab inactive">Sectors</div>
  </div>
  <div class="tab-panel body-text">
    <span class="more">more +</span>
    <ul class="bullets">
      <li>On time and within budget</li>
      <li>Project leadership</li>
      <li>Researched inputs and facilitated outcomes</li>
      <li>Focus on implementation</li>
      <li>Develop value</li>
      <li>adding partnerships and get them funded</li>
      <li>Creative responses to funding opportunities</li>
      <li>Organisational reviews</li>
    </ul>
  </div>
</section>

<section class="quotes abs">
  <div class="panel-head">
    <h2 class="section-title">Quotes</h2>
    <div class="pager">
      <span><svg width="7" height="10"><path d="M6 1L2 5l4 4" stroke="#e8562a" stroke-width="2" fill="none"/></svg></span>
      <span><svg width="7" height="10"><path d="M1 1l4 4-4 4" stroke="#e8562a" stroke-width="2" fill="none"/></svg></span>
    </div>
  </div>
  <div class="rule"></div>
  <p class="quote-text body-text"><svg class="quote-mark" width="10" height="9"><rect x="0" y="0" width="3" height="9" fill="#17618a"/><rect x="6" y="0" width="3" height="9" fill="#17618a"/></svg>The Halvern Group helped me out with my company problems located at very basic level. They repaired our roots!</p>
  <p class="quote-by body-text">- Owen Tarrick</p>
  <p class="quote-role">CEO, BRIGHTFIELD</p>
</section>

<section class="careers abs">
  <div class="panel-head">
    <h2 class="section-title">Careers</h2>
    <div class="pager">
      <span><svg width="7" height="10"><path d="M6 1L2 5l4 4" stroke="#e8562a" stroke-width="2" fill="none"/></svg></span>
      <span><svg width="7" height="10"><path d="M1 1l4 4-4 4" stroke="#e8562a" stroke-width="2" fill="none"/></svg></span>
    </div>
  </div>
  <div class="rule"></div>
  <div class="job body-text"><a href="#">Senior Consultant (LPD)</a><em>Melbourne</em></div>
  <div class="job body-text"><a href="#">Senior Consultant (LPD)</a><em>Melbourne</em></div>
  <div class="job body-text"><a href="#">Senior Consultant (LPD)</a><em>Melbourne</em></div>
  <a class="all-offers body-text" href="#">+ All offers</a>
</section>

<div class="partners-title abs"><h2 class="section-title">Key partners</h2></div>
<section class="partners abs" aria-label="Key partners">
  <div class="partner-row">
    <span class="partner-mark" style="width:24px;height:22px;border-radius:50%"></span>
    <span class="partner-mark" style="width:140px;height:16px"></span>
    <span class="partner-mark" style="width:22px;height:20px"></span>
    <span class="partner-mark" style="width:88px;height:16px"></span>
    <span class="partner-mark" style="width:70px;height:16px;background:#9a9a9a"></span>
    <span class="partner-mark" style="width:140px;height:16px"></span>
  </div>
</section>

<footer class="site-footer abs">
  <div class="contact-line abs">Contact us: (+48) 702 455 316</div>
  <div class="legal abs"><span>Design &amp; coding, 2013. All rights reserved</span><span>sitemap | privacy policy</span></div>
  <div class="connect abs">Connect:
    <div class="social" aria-label="Social links"><span></span><span></span><span></span></div>
  </div>
</footer>

</body>
</html>
```